Company web site

Looking for a full responsive(mobile friendly) wordpress implementation

Some material is in the website -- vantorelq.examplepress.com

But looking for a template more consistent with the logo design, and more future looking.

Target Market(s)

Enterprise Clients

Industry/Entity Type

It Company

Font styles to use
Sans Serif

Colors
33a6d7
0255a3
0455a3
cfdeed
85abd2
3176b5

Requirements
Must have
• about, contact information, partner page, success stories, customer testimonials. links to social presence.
• pricing information

```html
<!DOCTYPE html>
<html lang="en">
<head>
<meta charset="utf-8">
<title>Vantorelq — Contact</title>
<link rel="stylesheet" href="https://fonts.googleapis.com/css2?family=Questrial&family=Titillium+Web:wght@700&display=swap">
<style>
  :root {
    --ink: #0e1217;
    --header-dark: #1e232d;
    --brand-blue: #23a9e1;
    --band-blue: #9cc3e6;
    --panel-light: #d2e4f3;
    --panel-mid: #4f96bf;
    --strip: rgba(190, 215, 232, 0.55);
    --accent: #33a6d7;
    --deep: #0255a3;
    --text-dark: #111;
    --text-light: #eef3f8;
  }
  * { box-sizing: border-box; margin: 0; padding: 0; }
  html, body { width: 1200px; height: 1056px; overflow: hidden; }
  body { font-family: "Questrial", sans-serif; background: var(--band-blue); }
  .canvas { position: relative; width: 1200px; height: 1056px; overflow: hidden; background: var(--band-blue); }
  .backdrop { position: absolute; inset: 0; }
  .site-header { position: absolute; left: 0; top: 0; width: 1200px; height: 318px; }
  .utility-nav { position: absolute; right: 32px; top: 4px; display: flex; }
  .utility-nav a { color: var(--text-light); text-decoration: none; font-size: 21px; padding: 0 21px; line-height: 30px; border-left: 2px solid var(--text-light); }
  .utility-nav a:first-child { border-left: none; }
  .brand { position: absolute; left: 232px; top: 100px; display: flex; align-items: center; gap: 28px; }
  .brand-dot { width: 88px; height: 88px; border-radius: 50%; background: var(--brand-blue); }
  .brand-name { font-size: 128px; line-height: 1; color: var(--brand-blue); letter-spacing: 2px; }
  .main-nav { position: absolute; left: 0; top: 330px; width: 1200px; height: 40px; }
  .main-nav a { position: absolute; top: 0; height: 38px; line-height: 38px; text-align: center; font-family: "Titillium Web", sans-serif; font-weight: 700; font-size: 27px; color: var(--brand-blue); text-decoration: none; letter-spacing: 1px; }
  .contact-panel { position: absolute; left: 38px; top: 470px; }
  .page-title { font-size: 96px; font-weight: 400; color: var(--text-dark); letter-spacing: 3px; line-height: 1; }
  .contact-form { position: absolute; left: 0; top: 106px; width: 280px; }
  .contact-form label { display: block; font-size: 18px; color: var(--text-dark); line-height: 20px; }
  .contact-form input, .contact-form textarea { display: block; width: 274px; border: 1px solid #555; border-radius: 3px; background: transparent; margin: 2px 0 0 1px; }
  .contact-form input { height: 16px; margin-bottom: 20px; }
  .contact-form textarea { height: 90px; resize: none; margin-bottom: 14px; }
  .contact-form button { font-family: Arial, sans-serif; font-size: 16px; width: 78px; height: 23px; background: #d6d6d6; border: 1px solid #777; margin-left: 2px; color: #111; }
  .info-heading { position: absolute; font-size: 27px; color: #111; }
  .location-map { position: absolute; left: 926px; top: 520px; width: 238px; height: 174px; background: linear-gradient(135deg, #e3e3e3, #d4d4d4 60%, #ececd8); border: 1px solid #fff; }
  .address-card { position: absolute; left: 928px; top: 746px; width: 230px; height: 84px; border-radius: 4px; background: rgba(150, 195, 222, 0.65); padding: 8px 14px; font-size: 17px; line-height: 22px; color: #111; letter-spacing: 1px; word-spacing: 5px; }
  .site-footer { position: absolute; left: 0; top: 957px; width: 1200px; height: 99px; background: var(--ink); }
  .social-links { position: absolute; right: 62px; top: 12px; display: flex; gap: 18px; }
  .social-links a { display: flex; flex-direction: column; align-items: center; gap: 3px; color: #e6e6e6; text-decoration: none; font-size: 11px; }
  .social-links span.mark { width: 40px; height: 40px; border-radius: 5px; background: #e6e6e6; }
  .footer-link { position: absolute; right: 62px; bottom: 8px; color: var(--brand-blue); font-family: Arial, sans-serif; font-size: 13px; text-decoration: none; }
</style>
</head>
<body>
<div class="canvas">
  <svg class="backdrop" width="1200" height="1056" viewBox="0 0 1200 1056" aria-hidden="true">
    <defs>
      <radialGradient id="glow" cx="0.65" cy="0.55" r="0.6">
        <stop offset="0" stop-color="#33a6d7" stop-opacity="0.55"/>
        <stop offset="1" stop-color="#33a6d7" stop-opacity="0"/>
      </radialGradient>
    </defs>
    <rect width="1200" height="318" fill="#0e1217"/>
    <polygon points="160,0 1200,0 1200,40 512,112" fill="#1e232d"/>
    <polygon points="0,0 160,0 512,112 512,256 0,300" fill="#15191f"/>
    <polygon points="0,300 512,256 1200,256 1200,318 0,318" fill="#161b22"/>
    <rect y="318" width="1200" height="639" fill="#9cc3e6"/>
    <rect y="318" width="1200" height="639" fill="url(#glow)"/>
    <polygon points="0,384 810,428 810,880 0,908" fill="#d2e4f3" opacity="0.92"/>
    <polygon points="838,464 1200,416 1200,892 838,848" fill="#4f96bf"/>
    <polygon points="860,480 1200,480 1200,514 864,514" fill="rgba(190,215,232,0.55)"/>
    <polygon points="860,698 1200,698 1200,730 864,730" fill="rgba(190,215,232,0.55)"/>
    <polygon points="22,332 176,332 170,368 26,368" fill="#161b22"/>
    <polygon points="178,332 366,332 374,368 174,368" fill="#161b22"/>
    <polygon points="370,332 576,332 574,368 380,368" fill="#161b22"/>
    <polygon points="580,332 776,332 770,368 578,368" fill="#161b22"/>
    <polygon points="780,332 974,332 962,368 772,368" fill="#161b22"/>
    <polygon points="986,326 1168,326 1162,368 970,368" fill="#05070a"/>
    <polygon points="970,368 1162,368 1158,376 978,378" fill="#5b6c7a"/>
  </svg>

  <header class="site-header">
    <nav class="utility-nav">
      <a href="#">LOGIN</a><a href="#">SUPPORT</a><a href="#">CONTACT</a><a href="#">PRIVACY POLICY</a>
    </nav>
    <div class="brand">
      <span class="brand-dot"></span>
      <span class="brand-name">Vantorelq</span>
    </div>
  </header>

  <nav class="main-nav">
    <a href="#" style="left:22px;width:154px">HOME</a>
    <a href="#" style="left:178px;width:192px">PLATFORM</a>
    <a href="#" style="left:376px;width:200px">PARTNERS</a>
    <a href="#" style="left:578px;width:196px">BLOG</a>
    <a href="#" style="left:780px;width:188px">ABOUT</a>
    <a href="#" style="left:976px;width:186px;top:-4px">CONTACT</a>
  </nav>

  <main class="contact-panel">
    <h1 class="page-title">CONTACT</h1>
    <form class="contact-form">
      <label for="name">Your Name:</label>
      <input id="name" type="text">
      <label for="email">Email Address:</label>
      <input id="email" type="email">
      <label for="message">Your&nbsp; Message:</label>
      <textarea id="message"></textarea>
      <button type="button">SUBMIT</button>
    </form>
  </main>

  <h2 class="info-heading" style="left:896px;top:480px">Location</h2>
  <div class="location-map" role="img" aria-label="Street map showing the office location"></div>
  <h2 class="info-heading" style="left:896px;top:696px">Address</h2>
  <address class="address-card" style="font-style:normal">
    418 Harlow Ave<br>Merriton, CA 90417<br>+1-(555) 014-2738
  </address>

  <footer class="site-footer">
    <nav class="social-links">
      <a href="#"><span class="mark"></span>Repovault</a>
      <a href="#"><span class="mark"></span>Proflink</a>
      <a href="#"><span class="mark"></span>Pagecircle</a>
      <a href="#"><span class="mark"></span>Chirpline</a>
    </nav>
    <a class="footer-link" href="#">VANTORELQ.EXAMPLEPRESS.COM.</a>
  </footer>
</div>
</body>
</html>
```